Brochure Design Project for Family and Cosmetic Dental Practice

Family and Cosmetic Dental Practice with Ocean/Tropical Theme
Here is some more information about my business. We also have a website :www.marlowcrestsmiles.com. That has a video that we made and gives you a some more information about us.

An Overview / Background of the Business & Services :

Family and Cosmetic Dental Practice

Procedures that we do:

Clearmora (Clear Braces)

Dentures and Partials

Whitening/ Teeth Bleaching (both Brite and Vel)

Cosmetic Dentistry (veneers and esthetic crowns)

Implants

Children's Dentistry

Sedation Dentistry and Nitrous Oxide Gas (Laughing Gas)

The Target Market / Audience you are trying to reach:

Families (30 to 40 yrs with children) - Caucasians and Hispanics
People seeking cosmetic dentistry
Older Patients (50yrs +)

Design Specifics; any preferences or ideas for Style, Colour, Imagery, etc :

Color: Blues

Theme: Ocean/ Tropical

Our Philosophy

Our belief is that the best oral care that you receive is at home where you are able to maintain your oral hygiene through proper brushing, flossing and control of your diet. We would like to see you maintain your natural teeth for the rest of your life. When this is not possible we will work with you to replace them with the best aesthetic and functional restorative dentistry
that is available.

We want to let people we have been at our location for 10 years and we are family owned and are here for the long run. We are active in the community

Bios of the doctors: ( I already sent the headshot photos)

Dr Leonard Whitcombe
“Dr. Lenny”

Dr. Lenny Whitcombe attended Pemberton University for his undergraduate studies and earned a Bachelor’s degree in Chemistry. While attending Pemberton he pursued his passion of running and was a member of two Prairie Athletic League Champion cross country teams. His passion for running evolved into a desire to compete in triathlons. He continued his interest in the sciences and working with his hands by attending the Ashgrove State University College of Dentistry where he met his wife, Clara Whitcombe D.D.S. and earned his D.D.S. with honors in Oral Surgery. He has practiced the last few years in Tucson treating a wide range of patients. His desire to practice dentistry revolves around the patient and service. Some of his hobby highlights include finishing the Desert Ridge Endurance triathlon in 11 hours and 37 minutes in 2005 and a single digit golf handicap. His current passion is mountain biking. He recently finished the Ridgecrest Trail Cycling race (100 miles in one day)! Lately he spends a lot of time caring for and playing with his 3 daughters. Dr. Lenny Whitcombe is also a member of NOA (National Oral Alliance), StOC (State Oral Care Society) and GPF (Guild of Practice Fellows).

Dr. Clara Whitcombe
“Dr. Whitcombe”

Dr. Clara Whitcombe attended both Halvern College and Eastbrook Wesleyan College for her undergraduate degrees. She received a Bachelor of Science in Biology and a Bachelor of Arts in Psychology. After college, Dr Whitcombe worked for several years in the dental field while continuing her education by working towards a Master’s degree in Cell and Molecular Biology. At this point in her life Dr. Whitcombe knew that she enjoyed the dental field and decided to attend dental school. Dr. Whitcombe completed her Doctorate of Dental Surgery (D.D.S.) at Ashgrove State University where she met her husband, Dr. Leonard Whitcombe. They then moved to Tucson, Arizona in order to be close to family. When Dr. Clara isn't in the office creating beautiful smiles, she is busy with her 3 daughters and their numerous activities. Dr. Clara Whitcombe has additional training in the areas of endodontics and oral sedation. She is also a member of The National Guild of Practice Fellows (NGPF), National Oral Alliance (NOA), and State Oral Care Society (StOC). In her time outside of the office, Dr. Whitcombe enjoys traveling, spending time with her family, working out and being involved with book club.
Let me know if you need anything else!

Target Market(s)

See above

Industry/Entity Type

Business

Colors
33a6d7
85cae6
33b8a4

Requirements
Must have
• Testimonials taken from Rateway reviews. In any images used, the people must have nice smiles and teeth.

```html
<!DOCTYPE html>
<html lang="en">
<head>
<meta charset="utf-8">
<title>Marlowcrest Family Dentistry – Smile with confidence</title>
<link rel="stylesheet" href="https://fonts.googleapis.com/css2?family=Source+Sans+3:wght@400;600;700&display=swap">
<style>
  :root {
    --ocean: #33a6d7;
    --sky: #85cae6;
    --lagoon: #33b8a4;
    --deep-blue: #1f6fb4;
    --navy: #1c2a44;
    --ink: #2b2b2b;
    --sand: #e9c97a;
    --white: #ffffff;
  }
  * { box-sizing: border-box; margin: 0; padding: 0; }
  html, body { width: 755px; height: 1200px; overflow: hidden; background: var(--white); }
  body { font-family: "Source Sans 3", "Myriad Pro", sans-serif; color: var(--ink); }

  .flyer { position: relative; width: 755px; height: 1200px; overflow: hidden; background: var(--white); }

  .hero-scene {
    position: absolute; left: 0; top: 0; width: 755px; height: 700px;
    background:
      radial-gradient(ellipse 260px 340px at 560px 300px, rgba(214,170,140,0.55), rgba(214,170,140,0) 70%),
      linear-gradient(180deg,
        #4f9fd8 0%, #8cc8ec 22%, #cfe9f6 38%,
        #3fb3c9 44%, #2e9fc2 50%,
        var(--sand) 56%, #f1dca4 64%,
        #f7f3ea 76%, var(--white) 100%);
  }

  .brand {
    position: absolute; left: 60px; top: 20px; width: 250px; height: 96px;
    background: var(--white);
    display: flex; align-items: center; gap: 14px; padding: 0 14px;
  }
  .brand-mark { width: 46px; height: 46px; background: var(--navy); flex: none; }
  .brand-name {
    font-weight: 600; color: var(--navy); font-size: 21px; line-height: 1.05;
    letter-spacing: 2px; text-transform: uppercase;
  }

  .tagline { position: absolute; left: 100px; top: 292px; color: var(--navy); line-height: 1; }
  .tagline-lead { display: block; font-size: 44px; font-weight: 400; }
  .tagline-strong { display: block; font-size: 48px; font-weight: 700; margin-left: 80px; margin-top: 4px; }

  .procedures-header {
    position: absolute; left: 0; top: 650px; width: 755px; height: 46px;
    background: linear-gradient(90deg, var(--deep-blue) 0%, var(--ocean) 45%, rgba(51,166,215,0) 90%);
    display: flex; align-items: center; padding-left: 100px;
  }
  .procedures-header h2 { color: var(--white); font-size: 27px; font-weight: 700; }

  .procedures-rule { position: absolute; left: 100px; top: 700px; width: 600px; height: 1px; background: var(--sky); }

  .procedure-list { position: absolute; top: 722px; list-style: none; }
  .procedure-list.left { left: 100px; width: 330px; }
  .procedure-list.right { left: 466px; width: 250px; }
  .procedure-list li {
    position: relative; padding-left: 30px; margin-bottom: 18px;
    font-size: 21px; line-height: 1.2; color: var(--ink);
  }
  .procedure-list li::before {
    content: ""; position: absolute; left: 4px; top: 8px;
    width: 9px; height: 9px; border-radius: 50%; background: var(--ocean);
  }

  .philosophy { position: absolute; left: 100px; top: 996px; width: 610px; }
  .philosophy h3 { color: var(--ocean); font-size: 16px; font-weight: 700; margin-bottom: 6px; }
  .philosophy p { font-size: 14.5px; line-height: 1.32; color: var(--ink); margin-bottom: 10px; }
</style>
</head>
<body>
<main class="flyer">
  <div class="hero-scene" role="img" aria-label="Tropical beach with palm fronds, turquoise sea and soft clouds, with a smiling young man showing healthy teeth"></div>

  <div class="brand">
    <span class="brand-mark"></span>
    <span class="brand-name">Marlowcrest<br>Family<br>Dentistry</span>
  </div>

  <h1 class="tagline">
    <span class="tagline-lead">Smile with</span>
    <span class="tagline-strong">confidence</span>
  </h1>

  <div class="procedures-header"><h2>Procedures that we do:</h2></div>
  <div class="procedures-rule"></div>

  <ul class="procedure-list left">
    <li>Clearmora (Clear Braces)</li>
    <li>Dentures and Partials</li>
    <li>Whitening/ Teeth Bleaching (both Brite and Vel)</li>
    <li>Cosmetic Dentistry (veneers and esthetic crowns)</li>
  </ul>
  <ul class="procedure-list right">
    <li>Implants</li>
    <li>Children's Dentistry</li>
    <li>Sedation Dentistry and Nitrous Oxide Gas (Laughing Gas)</li>
  </ul>

  <section class="philosophy">
    <h3>Our Philosophy</h3>
    <p>Our belief is that the best oral care that you receive is at home where you are able to maintain your oral hygiene through proper brushing, flossing and control of your diet. We would like to see you maintain your natural teeth for the rest of your life. When this is not possible we will work with you to replace them with the best aesthetic and functional restorative dentistry that is available.</p>
    <p>We want to let people we have been at our location for 10 years and we are family owned and are here for the long run. We are active in the community</p>
  </section>
</main>
</body>
</html>
```